One business card required with 2 company logos and 2 people's details

One business card required.
No preference on design - One side could show the 2 different business logos for the companies we own. The reverse could have the details shown below.
Another option could be one business one side and one business on the reverse. Happy to receive designs.

Carol Denbigh
07700 318 274
Rachel Tolland
07700 582 036

website: truelymarvellous.example
email: info@truelymarvellous.example

website: ironwillowevents.example
email: info:ironwillowevents.example

May be nice to have icons instead of the words email/website?

I have included different versions of the logos to help with your design.

Contact Information for Business Card

see project overview

Requirements
Must have
• both company logos, both contact names and contact details

```html
<!DOCTYPE html>
<html lang="en">
<head>
<meta charset="utf-8">
<title>Business Card – Iron Willow Events &amp; Truely Marvellous</title>
<link rel="stylesheet" href="https://fonts.googleapis.com/css2?family=Open+Sans:wght@400;700&display=swap">
<style>
  :root {
    --stage: #8a8a8a;
    --card: #fbfbfa;
    --edge: #1f4fc0;
    --navy: #1d3d9c;
    --azure: #1f8fd0;
    --ink: #4a4a4a;
    --rule: #9a9a9a;
    --icon: #2a6fc7;
  }
  * { box-sizing: border-box; margin: 0; padding: 0; }
  html, body { width: 1200px; height: 801px; overflow: hidden; }
  body {
    background: var(--stage);
    font-family: "Open Sans", Arial, sans-serif;
    position: relative;
  }
  .card {
    position: absolute;
    top: 235px;
    width: 530px;
    height: 330px;
    background: var(--card);
    border-bottom: 3px solid var(--edge);
    border-left: 2px solid var(--edge);
  }
  .card--contacts { left: 45px; }
  .card--logos { left: 625px; }

  /* Contacts side */
  .contacts {
    position: absolute;
    inset: 0;
    display: flex;
    align-items: center;
    justify-content: center;
  }
  .person { width: 235px; padding: 0 18px; }
  .person--left { text-align: right; }
  .person--right { text-align: left; }
  .divider { width: 1px; height: 62px; background: var(--rule); align-self: flex-start; margin-top: 112px; }
  .person__name {
    font-weight: 700;
    font-size: 17px;
    letter-spacing: 0.2px;
    text-transform: uppercase;
    color: var(--navy);
    line-height: 1.2;
  }
  .person__name .surname { color: var(--azure); }
  .person__phone { font-size: 13px; color: var(--ink); margin-top: 2px; }
  .person__links { margin-top: 20px; }
  .link {
    display: flex;
    align-items: center;
    gap: 6px;
    font-size: 11.5px;
    color: var(--ink);
    line-height: 1.5;
  }
  .person--left .link { justify-content: flex-end; }
  .link svg { width: 11px; height: 11px; flex: none; }

  /* Logos side */
  .brands {
    position: absolute;
    inset: 0;
    display: flex;
    align-items: center;
    justify-content: space-around;
    padding: 0 30px;
  }
  .brand {
    display: flex;
    align-items: center;
    gap: 8px;
    font-weight: 700;
    font-size: 22px;
    line-height: 1.1;
    text-align: center;
  }
  .brand--willow { color: var(--edge); }
  .brand--marvellous { color: var(--navy); }
  .brand__dot { width: 14px; height: 14px; border-radius: 50%; flex: none; }
  .brand--willow .brand__dot { background: var(--edge); }
  .brand--marvellous .brand__dot { background: var(--navy); }
</style>
</head>
<body>
  <section class="card card--contacts" aria-label="Contact side">
    <div class="contacts">
      <div class="person person--left">
        <p class="person__name">Rachel <span class="surname">Tolland</span></p>
        <p class="person__phone">07700 582 036</p>
        <div class="person__links">
          <p class="link">info:ironwillowevents.example
            <svg viewBox="0 0 12 12" aria-hidden="true"><rect x="1" y="2.5" width="10" height="7" fill="var(--icon)"/><path d="M1 2.5 L6 6.5 L11 2.5" fill="none" stroke="#fff" stroke-width="1"/></svg>
          </p>
          <p class="link">ironwillowevents.example
            <svg viewBox="0 0 12 12" aria-hidden="true"><circle cx="6" cy="6" r="5" fill="var(--icon)"/><path d="M1 6 H11 M6 1 V11" stroke="#fff" stroke-width="0.8"/></svg>
          </p>
        </div>
      </div>
      <div class="divider"></div>
      <div class="person person--right">
        <p class="person__name">Carol <span class="surname">Denbigh</span></p>
        <p class="person__phone">07700 318 274</p>
        <div class="person__links">
          <p class="link">
            <svg viewBox="0 0 12 12" aria-hidden="true"><rect x="1" y="2.5" width="10" height="7" fill="var(--icon)"/><path d="M1 2.5 L6 6.5 L11 2.5" fill="none" stroke="#fff" stroke-width="1"/></svg>
            info@truelymarvellous.example</p>
          <p class="link">
            <svg viewBox="0 0 12 12" aria-hidden="true"><circle cx="6" cy="6" r="5" fill="var(--icon)"/><path d="M1 6 H11 M6 1 V11" stroke="#fff" stroke-width="0.8"/></svg>
            truelymarvellous.example</p>
        </div>
      </div>
    </div>
  </section>

  <section class="card card--logos" aria-label="Logo side">
    <div class="brands">
      <p class="brand brand--willow"><span class="brand__dot"></span>Iron Willow<br>Events</p>
      <p class="brand brand--marvellous"><span class="brand__dot"></span>Truely<br>Marvellous</p>
    </div>
  </section>
</body>
</html>
```